Zielgruppe
Wir sind ein Liechtensteiner Personaldienstleisungsunternehmen welches sowohl in der klassischen Personalvermittlung als auch in der temporären Personalbereitstellung tätig ist. Unsere Branchen reichen von Baugewerbe, Handwerk, Gastro- und Hotelerie bis hin zu Produktion und Gesundheitswesen.
Achtung:
Habe gerade die files vom neuen Logo hochgeladen!!!
Aufgabenstellung
Visitienkarten designen.
Briefpapier Vorlagenerstellung.
Schlichtes Visitenkartendesign Business auf der nicht zuviele Informationen sind (das Wichtigste)
Vorderseite:
Logo (wird vor Abschluss noch in besserer Qualität hochgeladen)
Firmenname
Anschrift
Name
Funktion
Telefon
Fax
E-Mail
Homepage
Rückseite:
Kann Kreativ gestaltet werden, farblich (blau, gelb, schwarz, weiss), nach Möglichkeit keinen weissen Hintergrund.
!!Bitte keine Vorschläge mit dem Fotoscanner ... da! Danke.
Wir freuen uns auch auf kreative Vorschläge, welche etwas vom Briefing abweichen.
TKV - Team

```html
<!DOCTYPE html>
<html lang="de">
<head>
<meta charset="utf-8">
<title>TKV Personal – Visitenkarte</title>
<link rel="stylesheet" href="https://fonts.googleapis.com/css2?family=Open+Sans:wght@400;600;700&display=swap">
<style>
  :root {
    --stage: #d2d7dc;
    --blue: #0d93d3;
    --blue-deep: #0883c6;
    --blue-light: #58b2e5;
    --yellow: #f4ea6e;
    --yellow-soft: #e6e46c;
    --black: #000000;
    --white: #ffffff;
    --ink: #1a1a1a;
    --card-w: 540px;
    --card-h: 310px;
  }
  * { box-sizing: border-box; margin: 0; padding: 0; }
  html, body {
    width: 1200px;
    height: 900px;
    overflow: hidden;
    background: var(--stage);
    font-family: "Open Sans", Arial, sans-serif;
  }
  .stage {
    position: relative;
    width: 1200px;
    height: 900px;
  }
  .card {
    position: absolute;
    top: 295px;
    width: var(--card-w);
    height: var(--card-h);
    overflow: hidden;
    background: var(--white);
    box-shadow: 0 3px 8px rgba(0, 0, 0, 0.18);
  }
  .card--back { left: 40px; }
  .card--front { left: 620px; }
  .card__shapes {
    position: absolute;
    inset: 0;
    width: 100%;
    height: 100%;
  }

  /* Back side */
  .back-mark {
    position: absolute;
    left: 150px;
    top: 98px;
    font-size: 96px;
    font-weight: 700;
    line-height: 1;
    color: var(--black);
    letter-spacing: 2px;
  }

  /* Front side */
  .brand {
    position: absolute;
    left: 36px;
    top: 44px;
    width: 150px;
    font-size: 26px;
    font-weight: 700;
    line-height: 1.15;
    color: var(--white);
  }
  .company {
    position: absolute;
    left: 232px;
    top: 46px;
    font-size: 17px;
    line-height: 1.35;
    letter-spacing: 1.2px;
    color: var(--ink);
  }
  .person {
    position: absolute;
    left: 228px;
    top: 132px;
    color: var(--ink);
  }
  .person__name {
    font-size: 20px;
    letter-spacing: 1px;
    line-height: 1.2;
  }
  .person__role {
    font-size: 13px;
    margin-top: 4px;
  }
  .contact {
    position: absolute;
    left: 222px;
    top: 202px;
    list-style: none;
    font-size: 15px;
    line-height: 1.7;
    color: var(--ink);
  }
  .contact__phone { letter-spacing: 1.6px; }
</style>
</head>
<body>
<main class="stage">

  <section class="card card--back" aria-label="Rückseite der Visitenkarte">
    <svg class="card__shapes" viewBox="0 0 540 310" preserveAspectRatio="none" aria-hidden="true">
      <rect width="540" height="310" fill="var(--blue)"/>
      <polygon points="0,40 0,70 105,78 55,35" fill="var(--white)"/>
      <polygon points="470,0 540,0 540,310 250,310 330,175" fill="var(--blue-light)"/>
      <polygon points="60,310 190,235 250,310" fill="var(--blue-light)"/>
      <polygon points="395,250 540,270 540,310 455,310" fill="var(--white)"/>
      <circle cx="410" cy="118" r="32" fill="var(--yellow-soft)"/>
    </svg>
    <div class="back-mark">TKV</div>
  </section>

  <section class="card card--front" aria-label="Vorderseite der Visitenkarte">
    <svg class="card__shapes" viewBox="0 0 540 310" preserveAspectRatio="none" aria-hidden="true">
      <polygon points="0,0 210,0 205,105 0,245" fill="var(--blue-deep)"/>
      <polygon points="400,0 540,0 540,100" fill="var(--black)"/>
      <polygon points="395,270 480,228 540,200 540,310 395,310" fill="var(--yellow)"/>
    </svg>

    <div class="brand">TKV<br>Personal</div>

    <address class="company" style="font-style: normal;">
      TKV Personal<br>
      Musterstrasse 1<br>
      12345 Musterstadt
    </address>

    <div class="person">
      <p class="person__name">Max Mustermann</p>
      <p class="person__role">Geschäftsführer</p>
    </div>

    <ul class="contact">
      <li class="contact__phone">Tel.: 0123456789</li>
      <li class="contact__phone">Fax: 0123456789</li>
      <li>email@tkv-personal.li</li>
      <li>www.tkv-personal.li</li>
    </ul>
  </section>

</main>
</body>
</html>
```